Managed Service Provider email

We need an email designed that advertises our Managed Services product. We have been in business 28 years. Managed Services includes proactive ticketing, Help desk support, server and workstation monitoring, data backup monitoring, spam protection, regular reports, Worklane 720, telecom services, ISP management, vendor management and more.

Target Market(s)

Business owners, decision makers, IT, CTO

Industry/Entity Type

Information Technology

Colors

Designer to choose colors to be used in the design.

Requirements
Must have
• Bullet points with included services. Mention of 28 years in business.
Nice to have
• We'd love our designer to read up on what an MSP (Managed Service Provider) does and use that information to find/create content for our email project.
Should not have
• A picture of a computer with a thermometer in its mouth.

```html
<!DOCTYPE html>
<html lang="en">
<head>
<meta charset="utf-8">
<title>Varden Network Services – Managed Services</title>
<link href="https://fonts.googleapis.com/css2?family=Audiowide&family=Arimo:wght@400;700&display=swap" rel="stylesheet">
<style>
  :root{
    --brand-blue:#1e8de0;
    --deep-blue:#0f3a66;
    --ink:#3a3d42;
    --body-grey:#6b6e73;
    --rule:#e8e9eb;
    --band:#f4f5f7;
    --footer:#3a3a3c;
    --white:#ffffff;
  }
  *{box-sizing:border-box;margin:0;padding:0}
  html,body{width:778px;height:1200px;overflow:hidden;background:var(--white)}
  body{position:relative;font-family:"Arimo",Arial,sans-serif;color:var(--body-grey)}
  .abs{position:absolute}
  .brand{left:42px;top:28px;font-family:"Audiowide",sans-serif;color:var(--ink);font-size:30px;line-height:1.1;display:flex;align-items:center;gap:10px}
  .brand-mark{width:22px;height:22px;border-radius:4px;background:var(--brand-blue)}
  .hero{left:0;top:0}
  .headline{left:37px;top:184px;font-family:"Audiowide",sans-serif;color:var(--white);font-size:25px;letter-spacing:.5px}
  .services{left:10px;top:252px}
  .service-list{left:96px;top:291px;list-style:none}
  .service-list li{height:27.2px;display:flex;align-items:center;color:var(--white);font-size:11.6px}
  .service-list li svg{margin-right:21px;flex:none}
  .welcome{left:340px;top:454px;width:400px;text-align:center}
  .welcome h2{font-family:"Audiowide",sans-serif;font-weight:400;font-size:17px;color:var(--ink);letter-spacing:.5px}
  .welcome h1{font-family:"Audiowide",sans-serif;font-weight:400;font-size:18.5px;color:var(--brand-blue);margin-top:8px;letter-spacing:.3px}
  .welcome p{font-size:11.4px;line-height:23.2px;margin-top:14px}
  .rule{left:6px;top:652px;width:764px;height:1px;background:var(--rule)}
  .feature-icon{width:70px;height:65px;border:2px solid var(--brand-blue);border-radius:16px;display:flex;align-items:center;justify-content:center}
  .feature h3{font-family:"Audiowide",sans-serif;font-weight:400;font-size:13.5px;color:var(--brand-blue);letter-spacing:.4px}
  .feature p{font-size:11.4px;line-height:23.2px;margin-top:12px;width:250px}
  .partners{left:0;top:864px;width:778px;height:336px;background:var(--band)}
  .partner-badge{top:903px;width:138px;height:78px;background:var(--white);border:1px solid #e3e4e7;box-shadow:0 1px 3px rgba(0,0,0,.08);display:flex;align-items:center;justify-content:center}
  .partner-badge span{display:block;width:86px;height:22px;border-radius:4px;background:#d7dadf}
  .partner-badge span.round{width:52px;height:52px;border-radius:50%}
  .footer{left:0;top:1000px}
  .contact{left:556px;list-style:none;color:#e9e9ea;font-size:11.4px}
  .contact li{display:flex;align-items:flex-start;gap:10px;line-height:14px}
  .copyright{left:9px;top:1157px;color:var(--white);font-size:11.6px}
</style>
</head>
<body>

<svg class="abs hero" width="778" height="430" viewBox="0 0 778 430">
  <defs>
    <linearGradient id="heroTone" x1="0" y1="0" x2="1" y2="1">
      <stop offset="0" stop-color="#2b4a6e"/>
      <stop offset=".5" stop-color="#1c3452"/>
      <stop offset="1" stop-color="#3f6d98"/>
    </linearGradient>
  </defs>
  <path role="img" aria-label="Photo of a hand reaching towards a glowing network globe over a blurred city"
        d="M0 84 C120 140 260 120 420 90 C560 62 680 40 778 70 L778 352 C720 410 620 425 560 410 C480 385 420 370 340 365 L0 360 Z"
        fill="url(#heroTone)"/>
  <path d="M340 362 C420 368 490 390 560 408 C640 428 720 405 778 352" fill="none" stroke="var(--brand-blue)" stroke-width="3"/>
</svg>

<div class="abs brand"><span class="brand-mark"></span><span>Varden Network Services</span></div>

<div class="abs headline">28 YEARS IN BUSINESS</div>

<svg class="abs services" width="350" height="352" viewBox="0 0 350 352">
  <circle cx="172" cy="172" r="170" fill="#bfc3c8"/>
  <circle cx="172" cy="179" r="170" fill="var(--brand-blue)"/>
</svg>

<ul class="abs service-list">
  <li><svg width="10" height="10" viewBox="0 0 10 10"><circle cx="5" cy="5" r="5" fill="#fff"/><path d="M3 5h4M5 3l2 2-2 2" stroke="var(--brand-blue)" stroke-width="1.4" fill="none"/></svg>Proactive Ticketing</li>
  <li><svg width="10" height="10" viewBox="0 0 10 10"><circle cx="5" cy="5" r="5" fill="#fff"/><path d="M3 5h4M5 3l2 2-2 2" stroke="var(--brand-blue)" stroke-width="1.4" fill="none"/></svg>Help Desk Support</li>
  <li><svg width="10" height="10" viewBox="0 0 10 10"><circle cx="5" cy="5" r="5" fill="#fff"/><path d="M3 5h4M5 3l2 2-2 2" stroke="var(--brand-blue)" stroke-width="1.4" fill="none"/></svg>Server &amp; Workstation Monitoring</li>
  <li><svg width="10" height="10" viewBox="0 0 10 10"><circle cx="5" cy="5" r="5" fill="#fff"/><path d="M3 5h4M5 3l2 2-2 2" stroke="var(--brand-blue)" stroke-width="1.4" fill="none"/></svg>Data Backup Monitoring</li>
  <li><svg width="10" height="10" viewBox="0 0 10 10"><circle cx="5" cy="5" r="5" fill="#fff"/><path d="M3 5h4M5 3l2 2-2 2" stroke="var(--brand-blue)" stroke-width="1.4" fill="none"/></svg>Spam Protection</li>
  <li><svg width="10" height="10" viewBox="0 0 10 10"><circle cx="5" cy="5" r="5" fill="#fff"/><path d="M3 5h4M5 3l2 2-2 2" stroke="var(--brand-blue)" stroke-width="1.4" fill="none"/></svg>Regular Reports</li>
  <li><svg width="10" height="10" viewBox="0 0 10 10"><circle cx="5" cy="5" r="5" fill="#fff"/><path d="M3 5h4M5 3l2 2-2 2" stroke="var(--brand-blue)" stroke-width="1.4" fill="none"/></svg>Worklane 720</li>
  <li><svg width="10" height="10" viewBox="0 0 10 10"><circle cx="5" cy="5" r="5" fill="#fff"/><path d="M3 5h4M5 3l2 2-2 2" stroke="var(--brand-blue)" stroke-width="1.4" fill="none"/></svg>Telecom Services</li>
  <li><svg width="10" height="10" viewBox="0 0 10 10"><circle cx="5" cy="5" r="5" fill="#fff"/><path d="M3 5h4M5 3l2 2-2 2" stroke="var(--brand-blue)" stroke-width="1.4" fill="none"/></svg>Isp Management</li>
  <li><svg width="10" height="10" viewBox="0 0 10 10"><circle cx="5" cy="5" r="5" fill="#fff"/><path d="M3 5h4M5 3l2 2-2 2" stroke="var(--brand-blue)" stroke-width="1.4" fill="none"/></svg>Vendor Management &amp; More</li>
</ul>

<section class="abs welcome">
  <h2>WELCOME TO</h2>
  <h1>VARDEN NETWORK SERVICES</h1>
  <p>Sed ut perspiciatis unde omnis iste natus error sit voluptatem accusantium doloremque laudantium, totam rem aperiam, eaque ipsa quae ab illo inventore veritatis et quasi arc hitecto beatae vitae dicta sunt explicabo. Nemo enim ips dolores eos qui ratione voluptatem sequi nesciunt.</p>
</section>

<div class="abs rule"></div>

<div class="abs feature-icon" style="left:10px;top:699px">
  <svg width="42" height="40" viewBox="0 0 42 40" fill="none" stroke="var(--brand-blue)" stroke-width="1.6">
    <circle cx="21" cy="20" r="4"/><circle cx="8" cy="8" r="4"/><circle cx="34" cy="8" r="3"/><circle cx="6" cy="26" r="3.5"/><circle cx="36" cy="24" r="4"/><circle cx="21" cy="35" r="3"/>
    <path d="M11 11l7 6M31 10l-7 7M9 25l8-4M32 23l-7-2M21 24v8"/>
  </svg>
</div>
<div class="abs feature" style="left:104px;top:699px">
  <h3>SED UT PERSPICIATIS</h3>
  <p>Sed ut perspiciatis unde omnis iste natus error sit voluptatem accusantium doloremque laudantium, totam rem aperiam, eaque ipsa quae ab illo inven beatae vitae dicta sunt explicabo</p>
</div>

<div class="abs feature-icon" style="left:421px;top:699px">
  <svg width="40" height="40" viewBox="0 0 40 40" fill="none" stroke="var(--brand-blue)" stroke-width="1.6">
    <circle cx="20" cy="10" r="7"/><circle cx="10" cy="28" r="7"/><circle cx="30" cy="28" r="7"/>
    <circle cx="20" cy="8.5" r="2"/><path d="M16.5 14c1-2.5 6-2.5 7 0"/>
    <circle cx="10" cy="26.5" r="2"/><path d="M6.5 32c1-2.5 6-2.5 7 0"/>
    <circle cx="30" cy="26.5" r="2"/><path d="M26.5 32c1-2.5 6-2.5 7 0"/>
  </svg>
</div>
<div class="abs feature" style="left:516px;top:699px">
  <h3>SED UT PERSPICIATIS</h3>
  <p>Sed ut perspiciatis unde omnis iste natus error sit voluptatem accusantium doloremque laudantium, totam rem aperiam, eaque ipsa quae ab illo inven beatae vitae dicta sunt explicabo</p>
</div>

<div class="abs partners"></div>
<div class="abs partner-badge" style="left:57px"><span></span></div>
<div class="abs partner-badge" style="left:233px"><span></span></div>
<div class="abs partner-badge" style="left:408px"><span class="round"></span></div>
<div class="abs partner-badge" style="left:584px"><span></span></div>

<svg class="abs footer" width="778" height="200" viewBox="0 0 778 200">
  <defs>
    <linearGradient id="footerTone" x1="0" y1="0" x2="0" y2="1">
      <stop offset="0" stop-color="#2c2c2e"/>
      <stop offset="1" stop-color="#454547"/>
    </linearGradient>
  </defs>
  <path d="M0 10 C60 60 140 80 260 70 C400 58 520 20 640 10 C700 5 750 10 778 20 L778 200 L0 200 Z" fill="url(#footerTone)"/>
</svg>

<ul class="abs contact" style="top:1085px">
  <li style="margin-bottom:13px"><svg width="13" height="12" viewBox="0 0 13 12" fill="#e9e9ea"><path d="M1 4C1 1 12 1 12 4v1H9V4H4v1H1z"/><rect x="2" y="6" width="9" height="6" rx="1"/></svg>Phone- 555-014-0404</li>
  <li style="margin-bottom:13px"><svg width="13" height="12" viewBox="0 0 13 12" fill="#e9e9ea"><rect x="3" y="0" width="7" height="4"/><rect x="0" y="4" width="13" height="5" rx="1"/><rect x="3" y="8" width="7" height="4"/></svg>Fax- 555-014-5554</li>
  <li><svg width="13" height="14" viewBox="0 0 13 14" fill="none" stroke="#e9e9ea" stroke-width="1.6"><path d="M6.5 13C3 9 2 7 2 5a4.5 4.5 0 019 0c0 2-1 4-4.5 8z"/><circle cx="6.5" cy="5" r="1.5"/></svg><span>1180 W Alder Row Brookfield,<br>ST 00000</span></li>
</ul>

<div class="abs copyright">© Copyright 2018 Varden Network Services.All Rights Reserved</div>

</body>
</html>
```